Web Design for Financial Consulting Company

We need a website design for a financial consulting company "Kelvane Consulting". We build financial models, scenario analysis, handle the budgeting process and provide temporary staffing. I have over 10 years of experience. My Excel expertise and analytical savvy has saved clients over $17 million in profit.

Target Market(s)

Small to medium businesses

Industry/Entity Type

Financial Consulting

Number of Pages Required

4 page

Requirements
Must have
• Professional looking
Nice to have
• A little futuristic looking

```html
<!DOCTYPE html>
<html lang="en">
<head>
<meta charset="utf-8">
<title>Kelvane Consulting</title>
<link rel="stylesheet" href="https://fonts.googleapis.com/css2?family=Outfit:wght@300;400;500;600;700&display=swap">
<style>
:root{
  --blue:#00b6ff;
  --blue-deep:#0a9fe6;
  --navy:#0d1a2b;
  --ink:#1b2433;
  --text:#3a4350;
  --muted:#6b7380;
  --card:#eef3f9;
  --white:#ffffff;
  --footer:#1a2331;
  --line:#d7dce3;
}
*{box-sizing:border-box;margin:0;padding:0}
html,body{width:1200px;height:2826px;overflow:hidden}
body{position:relative;font-family:"Outfit",sans-serif;color:var(--ink);background:var(--white)}
.abs{position:absolute}

/* hero */
.hero{left:0;top:0;width:1200px;height:628px;overflow:hidden}
.hero-photo{position:absolute;inset:0;background:linear-gradient(100deg,#1a2230 0%,#2b3442 35%,#4a5a6b 60%,#6d87a0 80%,#8aa3ba 100%)}
.hero-photo::after{content:"";position:absolute;inset:0;background:linear-gradient(90deg,rgba(10,16,26,.55) 0%,rgba(10,16,26,.15) 55%,rgba(0,0,0,0) 100%)}
.hero-cut{position:absolute;left:0;top:0}
.brand{display:flex;align-items:center;gap:10px;color:var(--white);font-weight:600;letter-spacing:.06em;text-transform:uppercase}
.brand-mark{width:26px;height:26px;background:var(--blue)}
.hero .brand{left:168px;top:31px;font-size:20px}
.nav{top:37px;display:flex;font-size:13.5px;color:var(--white);font-weight:500}
.nav a{position:absolute;white-space:nowrap;color:inherit;text-decoration:none}
.btn-outline{left:907px;top:28px;width:124px;height:35px;border:1.5px solid rgba(255,255,255,.85);border-radius:18px;color:var(--white);font-size:13.5px;font-weight:500;display:flex;align-items:center;justify-content:center;gap:8px}
.eyebrow{left:168px;top:201px;color:var(--blue);font-size:20px;font-weight:600;letter-spacing:.38em;display:flex;align-items:center;gap:10px}
.eyebrow::before{content:"";width:44px;height:1px;background:var(--blue)}
.hero-title{left:167px;top:236px;color:var(--white);font-size:48px;font-weight:600;line-height:54px}
.btn{display:flex;align-items:center;justify-content:center;gap:12px;background:var(--blue);color:var(--white);border-radius:24px;font-weight:500}
.hero .btn{left:169px;top:386px;width:191px;height:46px;font-size:18px}
.scroll-cue{left:578px;top:570px;width:44px;height:44px;background:var(--white);transform:rotate(45deg);box-shadow:0 4px 12px rgba(0,0,0,.18)}
.scroll-arrow{left:590px;top:582px}

/* about */
.h2{font-size:38px;font-weight:700;color:var(--navy)}
.about-title{left:0;top:676px;width:1200px;text-align:center}
.about-photo{left:0;top:750px;width:609px;height:406px;background:linear-gradient(120deg,#3f5566 0%,#6f7d86 40%,#3a3f46 70%,#1f252c 100%)}
.about-rule{left:658px;top:752px;width:1px;height:128px;background:var(--blue)}
.about-text{left:655px;top:908px;width:380px;font-size:16px;line-height:25.8px;color:var(--text)}
.about-text em{font-style:normal;color:var(--blue)}
.link{left:654px;top:1131px;color:var(--blue);font-size:17px;text-decoration:underline;text-underline-offset:3px;display:flex;align-items:center;gap:10px}

/* services */
.services{left:0;top:1231px;width:1200px;height:625px;background:var(--blue)}
.services-title{left:170px;top:1320px;color:var(--white)}
.title-rule{height:1px;background:currentColor}
.services-rule{left:170px;top:1376px;width:130px;color:var(--white)}
.services-intro{left:170px;top:1399px;width:250px;color:var(--white);font-size:13.5px;line-height:21.4px}
.card{width:267px;height:229px;background:var(--card);border-radius:8px;padding:0 28px}
.card.is-first{background:var(--white)}
.card svg{position:absolute;left:28px;top:38px}
.card h3{position:absolute;left:29px;top:114px;width:215px;font-size:14.5px;font-weight:600;line-height:21px;color:var(--navy);text-transform:uppercase}
.card p{position:absolute;left:29px;width:215px;font-size:13px;line-height:19.5px;color:var(--muted)}

/* contact */
.contact-title{left:169px;top:1925px}
.contact-rule{left:170px;top:1980px;width:130px;color:var(--blue)}
.contact-intro{left:170px;top:1995px;width:360px;font-size:13px;line-height:20px;color:var(--text)}
.field{border:1px solid var(--line);border-radius:4px;font-size:11.5px;color:var(--text);padding:12px 11px}
.contact .btn{left:420px;top:2340px;width:190px;height:46px;font-size:17px}
.contact-photo{left:664px;top:1931px;width:367px;height:460px;background:linear-gradient(160deg,#c9d6de 0%,#8aa0ad 35%,#4a5c6b 70%,#2b3641 100%)}

/* footer */
.footer{left:0;top:2466px;width:1200px;height:360px;background:var(--footer)}
.footer .brand{left:0;top:2545px;width:1200px;justify-content:center;font-size:30px}
.footer .brand-mark{width:34px;height:34px}
.footer-nav{top:2633px;color:#e4e8ee;font-size:15.5px;font-weight:400;text-transform:uppercase}
.footer-sep{top:2635px;width:1px;height:16px;background:#3b4656}
.footer-line{top:2722px;height:1px;background:#2f3a4a}
.social{top:2704px;width:36px;height:36px;border-radius:50%;background:var(--blue)}
.copyright{left:0;top:2777px;width:1200px;text-align:center;color:#d6dbe3;font-size:12.5px}
</style>
</head>
<body>

<section class="abs hero">
  <div class="hero-photo" role="img" aria-label="Photo of a smiling consultant in a light blue shirt at a meeting table with a laptop showing charts"></div>
  <svg class="hero-cut" width="1200" height="628" viewBox="0 0 1200 628">
    <polygon points="0,628 620,590 1200,555 1200,628" fill="#ffffff"/>
    <polygon points="630,590 1200,555 1200,614 880,602" fill="#00b6ff"/>
    <polygon points="630,590 1200,580 1200,596 880,598" fill="#0a9fe6"/>
  </svg>
  <div class="abs brand"><span class="brand-mark"></span>Kelvane Consulting</div>
  <nav class="abs nav">
    <a style="left:650px">Home</a>
    <a style="left:738px">About</a>
    <a style="left:827px">Services</a>
  </nav>
  <div class="abs btn-outline">Contact Us
    <svg width="12" height="10" viewBox="0 0 12 10"><path d="M1 5h9M6.5 1.5 10 5l-3.5 3.5" stroke="#fff" stroke-width="1.6" fill="none"/></svg>
  </div>
  <div class="abs eyebrow">Helping Your</div>
  <h1 class="abs hero-title">Finance Team &amp;<br>increasing profit</h1>
  <div class="abs btn">Get Started
    <svg width="15" height="12" viewBox="0 0 15 12"><path d="M1 6h12M8 1.5 12.5 6 8 10.5" stroke="#fff" stroke-width="2" fill="none"/></svg>
  </div>
  <div class="abs scroll-cue"></div>
  <svg class="abs scroll-arrow" width="20" height="20" viewBox="0 0 20 20"><path d="M10 3v13M5 11l5 5 5-5" stroke="#0d1a2b" stroke-width="2" fill="none"/></svg>
</section>

<section class="about">
  <h2 class="abs h2 about-title">About Us</h2>
  <div class="abs about-photo" role="img" aria-label="Photo of a businesswoman speaking with colleagues around a meeting table"></div>
  <div class="abs about-rule"></div>
  <svg class="abs" style="left:655px;top:876px" width="7" height="6" viewBox="0 0 7 6"><path d="M0 0h7L3.5 6z" fill="#00b6ff"/></svg>
  <p class="abs about-text">I am an experienced Finance professional who develops strategic financial plans, provides insightful analysis, and supports decision-making. With over <em>10 years</em> of experience, I have successfully increased profitability for clients by <em>$17M.</em></p>
  <a class="abs link">Learn More
    <svg width="16" height="12" viewBox="0 0 16 12"><path d="M1 6h13M9 1.5 13.5 6 9 10.5" stroke="#00b6ff" stroke-width="1.8" fill="none"/></svg>
  </a>
</section>

<section class="abs services"></section>
<h2 class="abs h2 services-title">Our Services</h2>
<div class="abs title-rule services-rule"></div>
<svg class="abs" style="left:297px;top:1373px" width="5" height="7" viewBox="0 0 5 7"><path d="M0 0l5 3.5L0 7z" fill="#fff"/></svg>
<p class="abs services-intro">Lorem Ipsum is simply dummy text of the printing and typesetting industry. Lorem Ipsum has been the industry's standard dummy text ever since the 1500s,</p>

<article class="abs card is-first" style="left:467px;top:1305px">
  <svg width="50" height="50" viewBox="0 0 50 50" fill="none" stroke="#00b6ff" stroke-width="1.6"><rect x="4" y="4" width="32" height="42" rx="2"/><path d="M10 14h14M10 20h10M10 40V32M16 40V28M22 40V34M28 40V30"/><circle cx="38" cy="20" r="8"/><path d="M38 15v10M35.5 17.5h4a1.5 1.5 0 0 1 0 3h-3a1.5 1.5 0 0 0 0 3h4"/></svg>
  <h3>Financial Models - Projects</h3>
  <p style="top:160px">Financial analysis, scenario modeling, pricing analysis, projects</p>
</article>
<article class="abs card" style="left:764px;top:1305px">
  <svg width="56" height="50" viewBox="0 0 56 50" fill="none" stroke="#00b6ff" stroke-width="1.6"><circle cx="15" cy="34" r="12"/><path d="M15 27v14M12 30h5a2 2 0 0 1 0 4h-4a2 2 0 0 0 0 4h5"/><circle cx="36" cy="12" r="6"/><circle cx="46" cy="32" r="6"/><circle cx="36" cy="12" r="2"/><circle cx="46" cy="32" r="2"/><path d="M4 16 14 8M10 8h4v4M48 8v-6M46 4l2-2 2 2"/></svg>
  <h3>Budgeting Process</h3>
  <p style="top:139px">Building budgets from scratch, revamping current process to be more robust and scalable.</p>
</article>
<article class="abs card" style="left:168px;top:1552px">
  <svg width="52" height="50" viewBox="0 0 52 50" fill="none" stroke="#00b6ff" stroke-width="1.6"><circle cx="26" cy="12" r="6"/><circle cx="13" cy="22" r="5"/><circle cx="39" cy="22" r="5"/><path d="M16 34c0-6 4-10 10-10s10 4 10 10M4 44c0-6 4-10 9-10M48 44c0-6-4-10-9-10M14 46c0-6 5-10 12-10s12 4 12 10"/></svg>
  <h3>Temporary Staffing</h3>
  <p style="top:139px">Years of Financial Planning and Analysis experience across multiple industries can help temporary staffing needs.</p>
</article>
<article class="abs card" style="left:467px;top:1552px">
  <svg width="50" height="50" viewBox="0 0 50 50" fill="none" stroke="#00b6ff" stroke-width="1.6"><path d="M10 4v22M4 44l6-18 6 18z"/><rect x="22" y="20" width="22" height="6"/><rect x="22" y="28" width="22" height="6"/><rect x="22" y="36" width="22" height="6"/><circle cx="38" cy="10" r="7"/><path d="M35 10l2 2 4-4"/><path d="M2 46h46"/></svg>
  <h3>Data Cleansing</h3>
  <p style="top:139px">Lorem Ipsum is simply dummy text of the printing and typesetting industry. Lorem Ipsum has...</p>
</article>
<article class="abs card" style="left:764px;top:1552px">
  <svg width="52" height="50" viewBox="0 0 52 50" fill="none" stroke="#00b6ff" stroke-width="1.6"><path d="M4 36 18 22l8 8 20-22M38 8h8v8"/><circle cx="22" cy="40" r="5"/><circle cx="22" cy="40" r="2"/><path d="M6 46h42M34 46V30M42 46V24"/></svg>
  <h3>Process Improvement:</h3>
  <p style="top:139px">Month end close, reporting, budgeting</p>
</article>

<section class="contact">
  <h2 class="abs h2 contact-title">Contact Us</h2>
  <div class="abs title-rule contact-rule"></div>
  <svg class="abs" style="left:297px;top:1977px" width="5" height="7" viewBox="0 0 5 7"><path d="M0 0l5 3.5L0 7z" fill="#00b6ff"/></svg>
  <p class="abs contact-intro">Lorem Ipsum is simply dummy text of the printing and typesetting industry. Lorem Ipsum has been the industry's standard dummy text ever since the 1500s,</p>
  <div class="abs field" style="left:169px;top:2084px;width:212px;height:38px">Name</div>
  <div class="abs field" style="left:398px;top:2084px;width:212px;height:38px">Email</div>
  <div class="abs field" style="left:169px;top:2135px;width:441px;height:38px">Subject</div>
  <svg class="abs" style="left:587px;top:2150px" width="11" height="7" viewBox="0 0 11 7"><path d="M1 1l4.5 4.5L10 1" stroke="#3a4350" stroke-width="1.4" fill="none"/></svg>
  <div class="abs field" style="left:169px;top:2185px;width:441px;height:124px">How can we help you?</div>
  <div class="abs btn">Submit Now
    <svg width="15" height="12" viewBox="0 0 15 12"><path d="M1 6h12M8 1.5 12.5 6 8 10.5" stroke="#fff" stroke-width="2" fill="none"/></svg>
  </div>
  <div class="abs contact-photo" role="img" aria-label="Photo of three business colleagues talking beside a glass office wall"></div>
</section>

<footer class="abs footer"></footer>
<div class="abs brand footer-brand" style="left:0;top:2545px;width:1200px;justify-content:center;font-size:30px"><span class="brand-mark" style="width:34px;height:34px"></span>Kelvane Consulting</div>
<nav>
  <span class="abs footer-nav" style="left:319px">Home</span>
  <span class="abs footer-sep" style="left:418px"></span>
  <span class="abs footer-nav" style="left:465px">About</span>
  <span class="abs footer-sep" style="left:570px"></span>
  <span class="abs footer-nav" style="left:617px">Services</span>
  <span class="abs footer-sep" style="left:739px"></span>
  <span class="abs footer-nav" style="left:786px">Contact Us</span>
</nav>
<div class="abs footer-line" style="left:168px;width:340px"></div>
<div class="abs footer-line" style="left:692px;width:340px"></div>
<span class="abs social" style="left:534px" aria-label="Social link"></span>
<span class="abs social" style="left:582px" aria-label="Social link"></span>
<span class="abs social" style="left:630px" aria-label="Social link"></span>
<p class="abs copyright">© 2023 KELVANE CONSULTING • BUILT WITH PRESSLINE</p>

</body>
</html>
```